4th Generation Family Business Needs a New Card Design!

We are a family owned 4th Generation company. We are based in the Sydney, Australia area and we are desperately in need of a more modern and classy card. We are monumental masons who design, supply & erect lasting memorials throughout cemeteries in Sydney. Our customers are normally in a period of grieving. I have attached logo files that will need to be implemented on the card. Company was established 1935. Australian Owned and Operated. Card needs to be designed to PRINTLY.com specification.

Target Market(s)

Our target market is based upon people that a grieving for family members that have passed away. We also deal with alot of companies that own and operate cemeteries.

Industry/Entity Type

Business

Contact Information for Business Card

Oliver Brantley, Operations Manager, 0417552908, oliver@hollowaystoneworks.com.au
Martin Brantley, Director, 0431906627, martin@hollowaystoneworks.com.au
Phone # 02 9634 2258
Website: www.hollowaystoneworks.com.au
Address: Suite 17, 8 Calloway Lane, East Penrose, Sydney NSW 2290

Font styles to use
Serif
Decorative
Script

Requirements
Must have
• Would like to see the logo nicely implemented with a modern design. Embossed lettering would be a nice additive.

```html
<!DOCTYPE html>
<html lang="en">
<head>
<meta charset="utf-8">
<title>Holloway Stoneworks – Business Card</title>
<link href="https://fonts.googleapis.com/css2?family=Cinzel:wght@400;600&family=Noto+Serif:wght@400&display=swap" rel="stylesheet">
<style>
  :root {
    --backdrop: #e4e4e4;
    --card-black: #0b0b0c;
    --card-sheen: #262729;
    --gold: #d6ab2a;
    --white: #ffffff;
    --text-soft: #d9d9d9;
    --faint-mark: rgba(255,255,255,0.035);
  }
  * { box-sizing: border-box; margin: 0; padding: 0; }
  html, body {
    width: 1200px; height: 576px; overflow: hidden;
    background: var(--backdrop);
  }
  .stage { position: relative; width: 1200px; height: 576px; }

  .card {
    position: absolute;
    width: 484px; height: 294px;
    top: 138px;
    background: linear-gradient(100deg, var(--card-black) 22%, var(--card-sheen) 40%, var(--card-black) 58%);
    overflow: hidden;
  }
  .card--front { left: 81px; }
  .card--back  { left: 602px; height: 292px; }

  .card__band {
    position: absolute; left: 0; right: 0; bottom: 0;
    height: 10px; background: var(--gold);
  }

  .brand {
    position: absolute;
    display: flex; flex-direction: column; align-items: center;
    font-family: "Cinzel", serif; font-weight: 600;
    color: var(--white); text-align: center; line-height: 1.05;
  }
  .brand__mark {
    width: 22px; height: 22px; border-radius: 50%;
    background: var(--gold); margin-bottom: 12px;
  }
  .brand__name { font-size: 34px; letter-spacing: 1px; }
  .brand__sub { font-size: 17px; letter-spacing: 3px; }

  .card--front .brand { left: 0; right: 0; top: 102px; }
  .card--back .brand { left: 22px; width: 230px; top: 110px; }
  .card--back .brand__name { font-size: 27px; }
  .card--back .brand__sub { font-size: 14px; }

  .faint-block {
    position: absolute; right: -30px; top: 30px;
    width: 220px; height: 240px;
    border: 14px solid var(--faint-mark);
  }

  .contact {
    position: absolute; left: 236px; top: 62px;
    font-family: "Noto Serif", serif; color: var(--text-soft);
  }
  .contact__name {
    font-family: "Cinzel", serif; font-weight: 400;
    font-size: 20px; color: var(--white); letter-spacing: 0.5px;
  }
  .contact__role { font-size: 11.5px; margin-top: 1px; }
  .contact__list { list-style: none; margin-top: 18px; }
  .contact__item {
    display: flex; align-items: center; gap: 9px;
    font-size: 12.5px; line-height: 17.5px;
  }
  .contact__item svg { width: 10px; height: 10px; fill: var(--gold); flex: none; }
  .contact__address { font-size: 12.5px; line-height: 18px; margin-top: 9px; }
</style>
</head>
<body>
<main class="stage">

  <section class="card card--front" aria-label="Card front">
    <div class="brand">
      <span class="brand__mark"></span>
      <span class="brand__name">Holloway</span>
      <span class="brand__sub">Stoneworks</span>
    </div>
    <div class="card__band"></div>
  </section>

  <section class="card card--back" aria-label="Card back">
    <div class="faint-block"></div>
    <div class="brand">
      <span class="brand__mark"></span>
      <span class="brand__name">Holloway</span>
      <span class="brand__sub">Stoneworks</span>
    </div>

    <div class="contact">
      <h1 class="contact__name">OLIVER BRANTLEY</h1>
      <p class="contact__role">Operations Manager</p>
      <ul class="contact__list">
        <li class="contact__item">
          <svg viewBox="0 0 10 10"><path d="M2 0.5 L3.6 0.5 L4.2 3 L3 3.8 Q4 6 6.2 7 L7 5.8 L9.5 6.4 L9.5 8 Q9.5 9.5 8 9.5 Q0.5 9 0.5 2 Q0.5 0.5 2 0.5Z"/></svg>
          0431906627
        </li>
        <li class="contact__item">
          <svg viewBox="0 0 10 10"><path d="M0.5 3 Q5 0 9.5 3 L9.5 4.3 L7.5 4.3 L7.5 3.4 L2.5 3.4 L2.5 4.3 L0.5 4.3Z M2 5 L8 5 L9 9.5 L1 9.5Z"/></svg>
          02 9634 2258
        </li>
        <li class="contact__item">
          <svg viewBox="0 0 10 10"><path d="M0.5 2 L9.5 2 L5 5.5Z M0.5 3 L5 6.5 L9.5 3 L9.5 8.5 L0.5 8.5Z"/></svg>
          martin@hollowaystoneworks.com.au
        </li>
        <li class="contact__item">
          <svg viewBox="0 0 10 10"><circle cx="5" cy="5" r="4.5"/></svg>
          www.hollowaystoneworks.com.au
        </li>
      </ul>
      <p class="contact__address">Suite 17, 8 Calloway Lane,<br>East Penrose, Sydney NSW 2290</p>
    </div>

    <div class="card__band"></div>
  </section>

</main>
</body>
</html>
```